Letterhead for 3 attorney Workers' Comp law firm

We are a 3 attorney law office. We specialize in Workers' Compensation. Our office represents workers who are injured on the job, and the estates of workers who are killed one the job.
When we started our office, we created our own letterhead & have been using it for years. We've just recently hired the 3rd attorney, and were going to just add his name to the letterhead, but have decided we wanted to get a professionally designed letterhead and business cards at this point.
We want something that looks clean and professional. It must look good in black and white because we often make multiple copies of our documents. We're hoping for a design that resonates confidence, reliability and experience.
The design must include the firm name: Thornbury & Calder, PLLC. We would like the PLLC to be small compared to the Thornbury & Calder graphic. We also want to incorporate the attorney names: Ivar Thornbury, Delia Calder, and Glen Rutledge. Our current letterhead has our contact info in the footer at the bottom of the page. We like that design, but are open to the idea of having it at the top. We'll leave that at the discretion of the designer. Our contact info is as follows: 482 S. Harrow Avenue, Suite 310 Bellingham, WA 98417 Phone: 360-555-2917, Fax: 360-555-4068, and our website: www.thornburycalder.example
Target Market(s)
Clients, courts, other legal offices, doctors offices. These are the people who see our letterhead most frequently. It's not so much for marketing purposes, mainly so that we have a professional image when sending out documents.
Industry/Entity Type
Law Firm
Contact Information for Business Card
On the back of the business card: it can be designed, or be a template for filling in appointment reminder information (i.e. date, time, etc)
Colors
Designer to choose colors to be used in the design.
Requirements
Must have
- Must have our firm name at the top.
- Must include the attorney names.
- Must have all of our contact information (can be at top or bottom - whatever looks best with the design)
Nice to have
- A strong, confident design
Should not have
- We don't want the design to be playful, cartoony or busy.

```html
<!DOCTYPE html>
<html lang="en">
<head>
<meta charset="utf-8">
<title>Thornbury &amp; Calder, PLLC — Stationery</title>
<link rel="stylesheet" href="https://fonts.googleapis.com/css2?family=Tinos&family=Raleway:wght@300;400&family=Arimo&display=swap">
<style>
  :root {
    --navy: #2e4a76;
    --name-grey: #9b9794;
    --ink: #6a6a6a;
    --accent-blue: #1f6fc4;
    --rule: #2e4a76;
    --paper: #ffffff;
    --backdrop: #e4e4e6;
  }
  * { margin: 0; padding: 0; box-sizing: border-box; }
  html, body { width: 1200px; height: 1200px; overflow: hidden; background: var(--backdrop); }
  .canvas { position: relative; width: 1200px; height: 1200px; }

  .firm-name { font-family: "Tinos", serif; color: var(--name-grey); text-align: center; line-height: 1; }
  .firm-name .title { display: block; }
  .firm-name .suffix { display: block; color: #ffffff; border-top: 1px solid var(--name-grey); }

  /* Letterhead */
  .letterhead { position: absolute; left: 198px; top: 213px; width: 512px; height: 724px; background: var(--paper); }
  .letterhead .band { height: 84px; background: var(--navy); display: flex; align-items: center; justify-content: center; }
  .letterhead .firm-name .title { font-size: 19px; }
  .letterhead .firm-name .suffix { font-size: 10px; margin-top: 3px; padding-top: 0; width: 136px; margin-left: auto; margin-right: auto; border-top: none; position: relative; }
  .letterhead .firm-name .suffix::after { content: ""; position: absolute; left: 0; right: 0; bottom: -2px; border-bottom: 1px solid var(--name-grey); }
  .letterhead .address-line { font-family: "Arimo", sans-serif; font-size: 8.4px; color: var(--navy); text-align: center; margin-top: 4px; }
  .headline { position: absolute; top: 138px; left: 0; width: 100%; text-align: center; font-family: "Raleway", sans-serif; font-weight: 400; font-size: 22px; letter-spacing: 0.3px; color: var(--ink); }
  .headline .highlight { color: var(--accent-blue); }
  .subhead { position: absolute; top: 172px; left: 162px; width: 200px; font-family: "Arimo", sans-serif; font-size: 8px; line-height: 10.5px; color: var(--ink); }
  .letter-body { position: absolute; top: 232px; left: 76px; width: 368px; font-family: "Raleway", sans-serif; font-weight: 400; font-size: 9.6px; letter-spacing: 0.45px; line-height: 14.65px; color: var(--ink); }
  .letter-body p + p { margin-top: 14.6px; }
  .signature-area { position: absolute; top: 537px; left: 76px; width: 72px; height: 22px; background: linear-gradient(90deg, #dcdcdc, #eeeeee); }
  .letter-footer { position: absolute; top: 607px; left: 17px; border-left: 1.5px solid var(--rule); padding-left: 8px; font-family: "Arimo", sans-serif; font-size: 8.3px; line-height: 13.6px; color: var(--ink); }
  .letter-footer .label { color: var(--navy); }
  .letter-footer .address { line-height: 10.5px; margin-top: 1px; }

  /* Business cards */
  .card { position: absolute; left: 796px; width: 219px; height: 122px; background: var(--paper); overflow: hidden; }
  .card-front { top: 411px; }
  .card-front .band { height: 38px; background: var(--navy); display: flex; align-items: center; justify-content: center; }
  .card .firm-name .title { font-size: 9px; }
  .card .firm-name .suffix { font-size: 5px; margin-top: 1px; border-top: none; border-bottom: 0.5px solid var(--name-grey); width: 70px; margin-left: auto; margin-right: auto; }
  .card-contacts { position: absolute; top: 63px; left: 0; width: 100%; display: flex; font-family: "Arimo", sans-serif; font-size: 5.6px; line-height: 10px; color: var(--ink); }
  .card-contacts .attorneys { width: 78px; text-align: right; padding-right: 7px; }
  .card-contacts .details { border-left: 0.8px solid var(--rule); padding-left: 8px; }
  .card-contacts .label { color: var(--navy); }
  .card-address { position: absolute; bottom: 2px; left: 0; width: 100%; text-align: center; font-family: "Arimo", sans-serif; font-size: 5.6px; color: var(--navy); }
  .card-back { top: 601px; background: var(--navy); display: flex; align-items: center; justify-content: center; }
  .card-back .firm-name .title { font-size: 13px; }
  .card-back .firm-name .suffix { font-size: 6.5px; width: 100px; }
</style>
</head>
<body>
<main class="canvas">

  <section class="letterhead" aria-label="Letterhead">
    <header>
      <div class="band">
        <div class="firm-name">
          <span class="title">Thornbury &amp; Calder</span>
          <span class="suffix">PLLC</span>
        </div>
      </div>
      <p class="address-line">482 S. Harrow Avenue, Suite 310 Bellingham, WA 98417</p>
    </header>

    <h1 class="headline">YOUR<span class="highlight">HEADLINE</span></h1>
    <p class="subhead">Lorem ipsum dolor sit amet, consectetuer adipi-scing elit, sed diam</p>

    <div class="letter-body">
      <p>Lorem ipsum dolor sit amet, consectetuer adipiscing elit, sed diam nonummy nibh euismod tincidunt ut laoreet dolore magna aliquam erat volutpat. Ut wisi enim ad minim veniam, quis nostrud exerci tation ullamcorper suscipit lobortis nisl ut aliquip ex ea commodo consequat. Duis autem vel eum iriure dolor in hendrerit in vulputate velit esse molestie consequat, vel illum dolore eu feugiat nulla facilisis at vero eros et accumsan et iusto odio dignissim qui bladit praesent luptatum zzril delenit augue duis dolore te feugait nulla facilisi.</p>
      <p>Nam liber tempor cum soluta nobis eleifend option congue nihil imperdiet doming id quod mazim placerat facer possim assum. Typi non habent claritatem insitam; est usus legentis in iis qui facit eorum claritatem. Investigationes demonstraverunt lectores legere me lius quod ii legunt saepius. Claritas est etiam processus dynamicus, qui sequitur mutationem consuetudium lectorum.</p>
      <p>Mirum est notare quam littera gothica, quam nunc putamus parum claram, anteposuerit litterarum formas humanitatis per seacula quarta decima et quinta decima. Eodem modo typi, qui nunc nobis videntur parum clari, fiant sollemnes in futurum.</p>
    </div>

    <div class="signature-area" role="img" aria-label="Handwritten signature"></div>

    <footer class="letter-footer">
      <div>Ivar Thornbury</div>
      <div>Delia Calder</div>
      <div>Glen Rutledge</div>
      <div><span class="label">Phone:</span> 360-555-2917</div>
      <div><span class="label">Fax:</span> 360-555-4068</div>
      <div><span class="label">Web:</span> www.thornburycalder.example</div>
      <div class="address"><span class="label">Adress:</span> 482 S. Harrow Avenue,<br>Suite 310 Bellingham, WA 98417</div>
    </footer>
  </section>

  <section class="card card-front" aria-label="Business card front">
    <div class="band">
      <div class="firm-name">
        <span class="title">Thornbury &amp; Calder</span>
        <span class="suffix">PLLC</span>
      </div>
    </div>
    <div class="card-contacts">
      <div class="attorneys">
        <div>Ivar Thornbury</div>
        <div>Delia Calder</div>
        <div>Glen Rutledge</div>
      </div>
      <div class="details">
        <div><span class="label">Phone:</span> 360-555-2917</div>
        <div><span class="label">Fax:</span> 360-555-4068</div>
        <div><span class="label">Web:</span> www.thornburycalder.example</div>
      </div>
    </div>
    <p class="card-address">482 S. Harrow Avenue, Suite 310 Bellingham, WA 98417</p>
  </section>

  <section class="card card-back" aria-label="Business card back">
    <div class="firm-name">
      <span class="title">Thornbury &amp; Calder</span>
      <span class="suffix">PLLC</span>
    </div>
  </section>

</main>
</body>
</html>
```